Redesign Web Page

I am looking for a great re-design and possibly a banner for TrueSpark.us. The site is for an online dating (self-development, online dating) book. The purpose is to drive book sales.

Target Market(s)

Women 18-55

```html
<!DOCTYPE html>
<html lang="en">
<head>
<meta charset="utf-8">
<title>True Spark</title>
<link rel="stylesheet" href="https://fonts.googleapis.com/css2?family=Source+Sans+3:wght@400;600&display=swap">
<style>
:root{
  --magenta:#bb106c;
  --magenta-text:#b8126d;
  --grey:#d2cbce;
  --card:#d9d1d5;
  --white:#ffffff;
  --ink:#1c1a1b;
  --photo-top:#5c6a3a;
  --photo-mid:#b89a72;
  --photo-low:#8d7a52;
}
*{margin:0;padding:0;box-sizing:border-box}
html,body{width:1200px;height:975px;overflow:hidden}
body{background:var(--magenta);font-family:"Source Sans 3",Arial,sans-serif;position:relative}
.brand{position:absolute;left:217px;top:20px;color:var(--white);font-size:37px;font-weight:400;letter-spacing:.5px}
.social{position:absolute;top:30px;right:217px;display:flex;gap:18px}
.social-link{display:flex;align-items:center;gap:6px;color:var(--white);font-size:15px;text-decoration:none}
.social-link i{width:14px;height:14px;background:var(--white);border-radius:3px;display:block}
.banner{position:absolute;left:216px;top:79px;width:769px;height:258px;background:var(--white);padding:7px 7px 7px 6px;box-shadow:2px 2px 4px rgba(0,0,0,.25)}
.banner-photo{width:100%;height:100%;background:linear-gradient(180deg,var(--photo-top) 0%,var(--photo-mid) 55%,var(--photo-low) 100%)}
.main-nav{position:absolute;left:217px;top:337px;width:767px;height:63px;background:var(--grey)}
.main-nav a{position:absolute;top:0;height:63px;line-height:63px;transform:translateX(-50%);color:var(--magenta-text);font-size:15px;text-decoration:none;white-space:nowrap}
.main-nav .current{left:0;transform:none;width:79px;text-align:center;background:var(--magenta);color:var(--white);border-left:2px solid var(--white)}
.features{position:absolute;top:433px;left:224px;display:flex;gap:17px}
.feature-card{width:175px;height:217px;background:var(--card);border-radius:6px;position:relative;padding:0 19px}
.feature-card h2{color:var(--magenta-text);font-weight:400;font-size:23px;line-height:27px;text-align:center;height:72px;display:flex;align-items:center;justify-content:center;padding-top:6px}
.feature-card p{font-size:13.5px;line-height:16.2px;text-align:justify;color:var(--ink);height:97px;overflow:hidden;hyphens:auto}
.feature-card .more{position:absolute;right:20px;bottom:10px;color:var(--magenta-text);font-size:13.5px;text-decoration:none}
.welcome{position:absolute;left:242px;top:670px;width:730px;color:var(--white)}
.welcome h1{font-size:16px;font-weight:400;margin-left:2px;margin-bottom:12px}
.welcome p{font-size:15.6px;line-height:19.8px;text-align:justify}
.site-footer{position:absolute;left:0;top:900px;width:1200px;height:75px;background:var(--grey);color:var(--ink);font-size:15px}
.site-footer .copyright{position:absolute;left:244px;top:21px}
.site-footer a{position:absolute;top:24px;transform:translateX(-50%);color:var(--ink);text-decoration:none;white-space:nowrap}
</style>
</head>
<body>
<header>
  <div class="brand">TRUE SPARK</div>
  <div class="social">
    <a class="social-link" href="#"><i></i>Circlebook</a>
    <a class="social-link" href="#"><i></i>Chirper</a>
  </div>
</header>
<div class="banner"><div class="banner-photo" role="img" aria-label="Photo of a happy couple embracing outdoors by the water"></div></div>
<nav class="main-nav">
  <a class="current" href="#">Home</a>
  <a href="#" style="left:123px">The Author</a>
  <a href="#" style="left:191px">Blog</a>
  <a href="#" style="left:266px">Fan Fair &amp; Fun</a>
  <a href="#" style="left:391px">Celeb Endorsements</a>
  <a href="#" style="left:503px">Love Stories</a>
  <a href="#" style="left:613px">Products &amp; Services</a>
  <a href="#" style="left:722px">Contact Us</a>
</nav>
<section class="features">
  <article class="feature-card"><h2>Buy A Book</h2><p>Lorem Ipsum is simply dummy text of the printing and typesetting industry. Lorem Ipsum has been the industry's standard dummy text ever since the 1500s.</p><a class="more" href="#">More</a></article>
  <article class="feature-card"><h2>Speak with Author</h2><p>Lorem Ipsum is simply dummy text of the printing and typesetting industry. Lorem Ipsum has been the industry's standard dummy text ever since the 1500s.</p><a class="more" href="#">More</a></article>
  <article class="feature-card"><h2>Popular Books</h2><p>Lorem Ipsum is simply dummy text of the printing and typesetting industry. Lorem Ipsum has been the industry's standard dummy text ever since the 1500s.</p><a class="more" href="#">More</a></article>
  <article class="feature-card"><h2>Authors talk</h2><p>Lorem Ipsum is simply dummy text of the printing and typesetting industry. Lorem Ipsum has been the industry's standard dummy text ever since the 1500s.</p><a class="more" href="#">More</a></article>
</section>
<section class="welcome">
  <h1>Welcome</h1>
  <p>Lorem Ipsum is simply dummy text of the printing and typesetting industry. Lorem Ipsum has been the industry's standard dummy text ever since the 1500s, when an unknown printer took a galley of type and scrambled it to make a type specimen book. It has survived not only five centuries, but also the leap into electronic typesetting, remaining essentially unchanged.</p>
  <p>Lorem Ipsum is simply dummy text of the printing and typesetting industry. Lorem Ipsum has been the industry's standard dummy text ever since the 1500s, when an unknown printer took a galley of type and scrambled it to make a type specimen book. It has survived not only five centuries, but also the leap into electronic typesetting, remaining essentially unchanged.</p>
</section>
<footer class="site-footer">
  <span class="copyright">Copyrights All Rights reserved</span>
  <a href="#" style="left:619px">Home</a>
  <a href="#" style="left:726px">Products &amp; Services</a>
  <a href="#" style="left:847px">Love Stories</a>
  <a href="#" style="left:941px">Contact Us</a>
</footer>
</body>
</html>
```